The Bean Lantern - Looking for a stylish, cool, hipster style logo and website look and feel.

We need a logo and screen design for an e-commerce website that offers a variety of coffee blends to customers.
We first need a logo, and subsequently a theme for the entire website.
The design can be hipster/rustic/stylish, as it fits in the barrister/coffee culture environment. We are imagining a black/white logo and theme, which can also use an additional accent colour (we are open to suggestions).
In short, what we need: 1. A logo "The Bean Lantern", and a selection of fonts/accent colours for our platform.

Target Market(s)

Our target market is customers who shop coffee online. They are typically between 25 and 50 years old and value a very clean, crisp, stylish, professional design.

Industry/Entity Type

Coffee Shop

Contact Information for Business Card

logo, company name, more details to follow

Logo Text

The Bean Lantern

Number of Pages Required

1 page

Font styles to use
Sans Serif

Colors
474747
333333
000000
ffffff

Requirements
Must have
• Please note that the market we are operating in is very stylish. Some examples of the industry here:
• https://www.quillharbour.com.au/
• http://marcoandfennels.com.au/
• It is essential that our design is stylish and cool.
Nice to have
• We are looking for a very stylish, cool, minimalistic (even hipster) look and feel.
• If more text is needed for a logo, you can add:
• Australia
• Australia's best roasters
• Speciality Coffee
Should not have
• Please no brown colour (as the association with coffee).

```html
<!DOCTYPE html>
<html lang="en">
<head>
<meta charset="utf-8">
<title>The Bean Lantern</title>
<link href="https://fonts.googleapis.com/css2?family=Roboto:ital,wght@0,400;0,500;0,700;1,700&display=swap" rel="stylesheet">
<style>
:root{
  --ink:#333333;
  --ink-soft:#474747;
  --black:#000000;
  --white:#ffffff;
  --page:#f8f8f8;
  --card:#efefef;
  --muted:#555555;
  --rule:#444444;
}
*{box-sizing:border-box;margin:0;padding:0}
html,body{width:1200px;height:1200px;overflow:hidden;background:var(--white);font-family:'Roboto',sans-serif;color:var(--ink)}
.stage{position:absolute;left:0;top:0;width:1500px;height:1500px;transform:scale(.8);transform-origin:0 0}
.stage *{position:absolute}
.page{left:440px;top:0;width:620px;height:1482px;background:var(--page)}
.photo-dark{background:radial-gradient(ellipse at 35% 55%,#5a5a5a 0%,#2a2a2a 45%,#111 100%)}
.hero{left:497px;top:0;width:505px;height:302px}
.brand{left:507px;top:8px;display:flex;align-items:center;gap:8px;position:absolute}
.brand *{position:static}
.brand-dot{width:22px;height:22px;border-radius:50%;border:2px solid var(--white)}
.brand-name{color:var(--white);font-weight:700;font-size:15px;line-height:30px;white-space:nowrap}
.nav{top:13px;height:18px;font-size:7.5px;font-weight:500;color:var(--white);line-height:18px;white-space:nowrap}
.nav-home{left:761px;width:35px;background:var(--white);color:var(--black);text-align:center}
.search{left:980px;top:13px;width:16px;height:16px;border-radius:50%;background:var(--white)}
.hero-title{left:497px;width:505px;top:112px;text-align:center;color:var(--white);font-size:32px;font-weight:700;letter-spacing:-.3px}
.hero-sub{left:497px;width:505px;top:152px;text-align:center;color:var(--white);font-size:15px;font-weight:500}
.btn-dark{background:#1d1d1d;color:var(--white);font-size:7px;font-weight:500;text-align:center;border:1px solid #3a3a3a;border-radius:2px}
.scroll-cue{left:734px;top:285px;width:32px;height:32px;border-radius:50%;background:var(--white);border:1px solid #ddd}
.section-title{left:497px;width:505px;text-align:center;font-size:18px;font-weight:500;color:var(--ink)}
.divider{left:682px;width:136px;height:10px}
.welcome-photo{left:710px;top:394px;width:80px;height:80px;background:linear-gradient(135deg,#b6b0aa,#6d625b 55%,#3b332f)}
.intro{left:507px;width:486px;top:485px;text-align:center;font-size:7.4px;line-height:13px;color:var(--muted)}
.card{top:569px;width:160px;height:234px;background:var(--card)}
.card *{position:absolute}
.card-title{left:0;width:100%;top:14px;text-align:center;font-size:22px;font-weight:700;line-height:26px;color:var(--ink)}
.card-kicker{left:0;width:100%;top:39px;text-align:center;font-size:14px;font-weight:500;color:var(--ink)}
.card-photo{left:31px;top:66px;width:98px;height:98px;border-radius:50%}
.card-text{left:8px;width:144px;top:175px;text-align:center;font-size:7.4px;line-height:11px;color:var(--muted)}
.card-btn{left:58px;top:208px;width:43px;height:17px;line-height:15px;border-radius:3px;font-size:7px;font-weight:700;text-align:center}
.card-btn.solid{background:var(--black);color:var(--white);border:1px solid var(--black)}
.card-btn.outline{background:var(--white);color:var(--ink);border:1px solid var(--ink)}
.band{left:497px;width:505px}
.band-title{left:497px;width:505px;text-align:center;color:var(--white);font-size:16px;font-weight:700}
.email{left:629px;top:898px;width:242px;height:21px;border-radius:11px;background:var(--white);font-size:7px;color:#999;line-height:21px;padding-left:10px}
.subscribe{left:714px;top:930px;width:71px;height:16px;border-radius:8px;background:var(--ink);color:var(--white);font-size:7px;font-weight:500;text-align:center;line-height:16px}
.price{top:1070px;width:116px;height:83px;background:var(--ink);color:var(--white)}
.price *{position:absolute}
.price-name{left:0;width:100%;top:7px;text-align:center;font-size:13px;font-weight:700}
.price-rule{left:40px;top:28px;width:36px;height:1px;background:var(--white)}
.price-cur{left:24px;top:45px;width:10px;height:11px;background:var(--white);color:var(--ink);font-size:8px;font-weight:700;text-align:center;line-height:11px}
.price-amt{left:40px;top:36px;font-size:33px;font-weight:700}
.avatar{left:546px;top:1262px;width:57px;height:53px;background:#cfcfcf;color:var(--ink);font-size:11px;font-weight:500;text-align:center;line-height:53px;border-radius:2px}
.review-text{left:617px;top:1262px;width:340px;color:#e6e6e6;font-size:7.4px;line-height:11.5px}
.review-by{left:620px;top:1302px;color:var(--white);font-size:7px;font-weight:700;font-style:italic}
.foot-head{top:1360px;font-size:8.5px;font-weight:700;color:var(--ink)}
.foot-head::after{content:"";position:absolute;left:0;bottom:-3px;width:20px;height:1px;background:var(--ink)}
.foot-list{top:1381px;font-size:6.8px;line-height:13px;color:var(--muted);list-style:none;white-space:nowrap}
.foot-list li{position:static}
.foot-list.arrow li::before{content:"› ";font-weight:700}
.social{top:1424px;width:18px;height:18px;border:1px solid #ccc;background:var(--white)}
.foot-rule{left:497px;top:1460px;width:505px;height:1px;background:#bbb}
.copyright{left:497px;width:505px;top:1467px;text-align:center;font-size:6.5px;color:var(--muted)}
</style>
</head>
<body>
<div class="stage">
  <div class="page"></div>

  <!-- Hero -->
  <div class="hero photo-dark" role="img" aria-label="Black and white photo of a steaming coffee cup on scattered coffee beans beside a burlap sack"></div>
  <div class="brand"><span class="brand-dot"></span><span class="brand-name">The Bean Lantern</span></div>
  <div class="nav nav-home">HOME</div>
  <div class="nav" style="left:816px">COFFEE ▾</div>
  <div class="nav" style="left:866px">SHOP</div>
  <div class="nav" style="left:897px">WHOLE SALE</div>
  <div class="search"><svg width="16" height="16" viewBox="0 0 16 16"><circle cx="7" cy="7" r="2.6" fill="none" stroke="#000" stroke-width="1.3"/><line x1="9" y1="9" x2="11.5" y2="11.5" stroke="#000" stroke-width="1.5"/></svg></div>
  <div class="hero-title">THE BEAN LANTERN</div>
  <div class="hero-sub">We love to serve you !</div>
  <div class="btn-dark" style="left:714px;top:188px;width:71px;height:19px;line-height:17px">Find Out More »</div>
  <div class="scroll-cue"><svg width="30" height="30" viewBox="0 0 30 30"><path d="M11 11l4 4 4-4M11 15l4 4 4-4" fill="none" stroke="#333" stroke-width="1.2"/></svg></div>

  <!-- Welcome -->
  <div class="section-title" style="top:344px">WELCOME TO OUR WEBSITE</div>
  <svg class="divider" style="top:369px" viewBox="0 0 136 10"><line x1="0" y1="5" x2="58" y2="5" stroke="#444"/><line x1="78" y1="5" x2="136" y2="5" stroke="#444"/><path d="M63 3h9v4a2 2 0 0 1-2 2h-5a2 2 0 0 1-2-2z" fill="#333"/><path d="M72 4h1.5a1.5 1.5 0 0 1 0 3H72" fill="none" stroke="#333"/><rect x="62" y="9" width="12" height="1" fill="#333"/></svg>
  <div class="welcome-photo" role="img" aria-label="Photo of hands placing a cup of latte on a wooden table"></div>
  <p class="intro">Lorem Ipsum is simply dummy text of the printing and typesetting industry. Lorem Ipsum has been the industry's standard dummy text ever since the 1500s, when an unknown printer took a galley of type and scrambled it to make a type specimen book. It has survived not only five centuries, but also the leap into electronic typesetting, remaining essentially unchanged. It was popularised in the 1960s with the release of Letraset sheets containing Lorem Ipsum passages, and more recently with desktop publishing software like Aldus PageMaker including versions of Lorem Ipsum.</p>

  <!-- Feature cards -->
  <div class="card" style="left:498px">
    <svg style="left:0;top:0" width="160" height="234" viewBox="0 0 160 234"><path d="M160 0V234H0z" fill="#dcdcdc"/></svg>
    <div class="card-title">100%</div>
    <div class="card-kicker">DELICIOUS</div>
    <div class="card-photo" role="img" aria-label="Photo of a latte with leaf foam art in a white cup" style="background:radial-gradient(circle at 55% 45%,#e9dccd 0%,#8a6c52 30%,#2d2520 75%)"></div>
    <div class="card-text">Lorem Ipsum is simply dummy text of the printing and typesetting industry.</div>
    <div class="card-btn outline">MORE ➜</div>
  </div>
  <div class="card" style="left:670px">
    <div class="card-title">SPICED</div>
    <div class="card-kicker">COFFEE</div>
    <div class="card-photo" role="img" aria-label="Photo of black coffee in a white cup surrounded by beans and spices" style="background:radial-gradient(circle at 50% 60%,#f2f2f2 0%,#1a1411 25%,#5b4334 55%,#2a1f19 100%)"></div>
    <div class="card-text">Lorem Ipsum is simply dummy text of the printing and typesetting industry.</div>
    <div class="card-btn solid">MORE ➜</div>
  </div>
  <div class="card" style="left:843px">
    <div class="card-title">HOT</div>
    <div class="card-kicker">OFFER</div>
    <div class="card-photo" role="img" aria-label="Photo of a steaming cup of coffee on a saucer against black" style="background:radial-gradient(circle at 50% 60%,#fafafa 0%,#6b4a36 22%,#d9d9d9 40%,#111 70%)"></div>
    <div class="card-text">Lorem Ipsum is simply dummy text of the printing and typesetting industry.</div>
    <div class="card-btn solid">MORE ➜</div>
  </div>

  <!-- Newsletter -->
  <div class="band photo-dark" style="top:828px;height:145px" role="img" aria-label="Dark photo of coffee beans, a cup and burlap"></div>
  <div class="band-title" style="top:845px">SUBSCRIBE US OUR NEWSLETTER</div>
  <svg class="divider" style="top:869px" viewBox="0 0 136 10"><line x1="0" y1="5" x2="58" y2="5" stroke="#fff"/><line x1="78" y1="5" x2="136" y2="5" stroke="#fff"/><path d="M62 5l12-5-4 10-2-4z" fill="none" stroke="#fff" stroke-width="1"/></svg>
  <div class="email">Email Address :</div>
  <div class="subscribe">SUBSCRIBE</div>

  <!-- Menu -->
  <div class="section-title" style="top:1009px">OUR BEST POSITIONS IN MENU</div>
  <svg class="divider" style="top:1033px" viewBox="0 0 136 10"><line x1="0" y1="5" x2="58" y2="5" stroke="#444"/><line x1="78" y1="5" x2="136" y2="5" stroke="#444"/><path d="M63 3h9v4a2 2 0 0 1-2 2h-5a2 2 0 0 1-2-2z" fill="#333"/><path d="M72 4h1.5a1.5 1.5 0 0 1 0 3H72" fill="none" stroke="#333"/><rect x="62" y="9" width="12" height="1" fill="#333"/></svg>
  <div class="price" style="left:498px"><div class="price-name">Lorem Ipsum</div><div class="price-rule"></div><div class="price-cur">$</div><div class="price-amt">10</div></div>
  <div class="price" style="left:627px"><div class="price-name">Lorem Ipsum</div><div class="price-rule"></div><div class="price-cur">$</div><div class="price-amt">17</div></div>
  <div class="price" style="left:757px"><div class="price-name">Lorem Ipsum</div><div class="price-rule"></div><div class="price-cur">$</div><div class="price-amt">22</div></div>
  <div class="price" style="left:886px"><div class="price-name">Lorem Ipsum</div><div class="price-rule"></div><div class="price-cur">$</div><div class="price-amt">40</div></div>

  <!-- Reviews -->
  <div class="band" style="top:1191px;height:146px;background:radial-gradient(ellipse at 80% 55%,#4a4a4a 0%,#1c1c1c 45%,#0a0a0a 100%)" role="img" aria-label="Dark photo of a coffee cup on a saucer"></div>
  <div class="band-title" style="top:1209px">PEOPLE REVIEW</div>
  <svg class="divider" style="left:698px;width:104px;top:1231px" viewBox="0 0 104 10"><line x1="0" y1="5" x2="42" y2="5" stroke="#fff"/><line x1="62" y1="5" x2="104" y2="5" stroke="#fff"/><path d="M47 3h9v4a2 2 0 0 1-2 2h-5a2 2 0 0 1-2-2z" fill="#fff"/><path d="M56 4h1.5a1.5 1.5 0 0 1 0 3H56" fill="none" stroke="#fff"/></svg>
  <div class="avatar">IMAGE</div>
  <p class="review-text">Lorem Ipsum is simply dummy text of the printing and typesetting industry. Lorem Ipsum has been the industry's standard dummy text ever since the 1500s, when an unknown printer took a galley of type and scrambled it to make a type specimen book.</p>
  <div class="review-by">LOREM IPSUM ( DUMMY TEXT )</div>

  <!-- Footer -->
  <div class="foot-head" style="left:502px">ADDRESS</div>
  <ul class="foot-list" style="left:502px;top:1382px;line-height:11.5px">
    <li>✆&nbsp;&nbsp; +61-0400 118 227</li>
    <li>✉&nbsp;&nbsp; hello@beanlantern.com.au</li>
    <li>⚲&nbsp;&nbsp; Lorem Ipsum (Dummy )</li>
  </ul>
  <div class="social" style="left:503px"></div>
  <div class="social" style="left:523px"></div>
  <div class="social" style="left:543px"></div>
  <div class="social" style="left:563px"></div>

  <div class="foot-head" style="left:633px">MAIN LINKS</div>
  <ul class="foot-list arrow" style="left:633px"><li>Home</li><li>About us</li><li>Whole shale</li><li>Cofeee shop</li><li>Sitemap</li></ul>

  <div class="foot-head" style="left:763px">COFFEES</div>
  <ul class="foot-list arrow" style="left:763px"><li>Hot Coffee</li><li>Cold Coffee</li><li>Espresso (Short Black)</li><li>Double Espresso (Doppio)</li><li>Long Black (Americano)</li></ul>

  <div class="foot-head" style="left:894px">OTHER LINKS</div>
  <ul class="foot-list arrow" style="left:894px"><li>Privacy Policy</li><li>Terms &amp; Use</li><li>Disclaimer</li></ul>

  <div class="foot-rule"></div>
  <div class="copyright">Copyright @ All Right Reserved 2017</div>
</div>
</body>
</html>
```